資格は全部で2種類あります。
各々コースが2つに分かれており、それぞれ初級・中級・上級があります。
コース・級ごとに色合いを変えていただければと思っております。
※デザイン2種:各6色(2つのコース×3つの級)の色合い変更

今回はコンペ形式にて1種類のデザインを募集させていただきます。
採用させていただいた方には、2種類ともデザインしていただければと思っております。

また、認定証のデザインをもとにした、認定カードのデザインもお願いいたします。
※認定証同様、デザイン2種各6色の色合い変更

採用報酬は、認定証・認定カードのすべてのデザインを含めた金額になります。
今回のコンペでは、下記2点の認定証のデザインを募集させていただきます。
①「創造育成指導員」という資格の「発達障がい支援コース」の「初級」
②「デジタル匠指導員」という資格の「IT実践コース」の「初級」

記載いただきたい項目は下記の通りになります。

・初級
・認定証
・発達障がい支援アドバイザー
・●●殿
・●●年●月●日
・あなたは当カリキュラムを修了されましたので、『初級・発達障がい支援アドバイザー』として認定いたします。
・NPO法人青葉学習推進会

・初級
・認定証
・IT実践アシスタント
・●●殿
・●●年●月●日
・あなたは当カリキュラムを修了されましたので、『初級・IT実践アシスタント』として認定いたします。
・NPO法人青葉学習推進会
認定証はカミノハコにて発注予定となっているため、イラストレーターのデータにて納品いただきますようお願いいたします。
テンプレートにつきましては、下記ギガファイル便のデータをご確認ください。
https://files.examplestore-transfer.jp/1008-a71c2e9b40f35d8862e1c7a04b5f2913e

また、ロゴや認定証のサンプルを添付させていただきます。
イラストレーターのデータにつきましては下記ギガファイル便をご確認ください。
https://files.examplestore-transfer.jp/1005-3b8e0f41c92d7a65e0b1f4d82c6a07e15

ゴールドを差し色とした素敵なデザインであったので選ばせていただきました。
ありがとうございました。

この度は弊社のコンペにご参加いただきありがとうございました。
また機会がございましたら、よろしくお願いいたします。

```html
<!DOCTYPE html>
<html lang="ja">
<head>
<meta charset="UTF-8">
<title>認定証 初級 発達障がい支援アドバイザー</title>
<link rel="stylesheet" href="https://fonts.googleapis.com/css2?family=Noto+Sans+JP:wght@400;500;700;900&display=swap">
<style>
  :root {
    --paper: #fbfbfb;
    --paper-tone: #f1f1f1;
    --ink: #222222;
    --rule: #9a9a9a;
    --gold-light: #f6e27a;
    --gold: #d9b43a;
    --gold-deep: #a9801c;
    --teal-light: #58c9b4;
    --teal: #1ea99a;
    --teal-deep: #0d7f7a;
    --org: #1d2f6b;
  }
  html, body {
    margin: 0;
    padding: 0;
    overflow: hidden;
    background: #ffffff;
  }
  .certificate {
    position: relative;
    width: 851px;
    height: 1200px;
    overflow: hidden;
    background: var(--paper);
    font-family: "Noto Sans JP", sans-serif;
    color: var(--ink);
  }
  .certificate__texture {
    position: absolute;
    inset: 0;
    background: radial-gradient(ellipse at 35% 45%, var(--paper) 0%, var(--paper-tone) 100%);
  }
  .certificate__ribbons {
    position: absolute;
    inset: 0;
  }
  .certificate__title {
    position: absolute;
    left: 42px;
    top: 300px;
    margin: 0;
    font-size: 74px;
    font-weight: 700;
    letter-spacing: 0.32em;
    line-height: 1;
  }
  .certificate__qualification {
    position: absolute;
    left: 42px;
    top: 422px;
    margin: 0;
    font-size: 40px;
    font-weight: 500;
    letter-spacing: 0.02em;
    line-height: 1;
  }
  .certificate__recipient {
    position: absolute;
    left: 42px;
    top: 520px;
    width: 568px;
    height: 80px;
    border-bottom: 2px solid var(--rule);
    display: flex;
    align-items: center;
    justify-content: center;
    gap: 14px;
  }
  .certificate__name {
    font-size: 58px;
    font-weight: 900;
    letter-spacing: 0.8em;
    line-height: 1;
  }
  .certificate__honorific {
    font-size: 34px;
    font-weight: 500;
    line-height: 1;
  }
  .certificate__date {
    position: absolute;
    left: 42px;
    top: 618px;
    margin: 0;
    font-size: 24px;
    font-weight: 500;
    line-height: 1;
  }
  .certificate__statement {
    position: absolute;
    left: 42px;
    top: 670px;
    width: 600px;
    margin: 0;
    font-size: 21px;
    font-weight: 400;
    line-height: 1.9;
  }
  .issuer {
    position: absolute;
    left: 0;
    width: 851px;
    top: 1070px;
    display: flex;
    align-items: center;
    justify-content: center;
    gap: 14px;
    color: var(--org);
  }
  .issuer__mark {
    width: 22px;
    height: 22px;
    border-radius: 50%;
    background: var(--org);
  }
  .issuer__name {
    font-size: 34px;
    font-weight: 700;
    letter-spacing: 0.04em;
    line-height: 1;
  }
</style>
</head>
<body>
<main class="certificate">
  <div class="certificate__texture" role="img" aria-label="淡いダマスク柄の背景"></div>

  <svg class="certificate__ribbons" width="851" height="1200" viewBox="0 0 851 1200" aria-hidden="true">
    <defs>
      <linearGradient id="gold-band" x1="0" y1="0" x2="1" y2="1">
        <stop offset="0" stop-color="var(--gold-light)"/>
        <stop offset="0.5" stop-color="var(--gold)"/>
        <stop offset="1" stop-color="var(--gold-light)"/>
      </linearGradient>
      <linearGradient id="teal-band" x1="0" y1="0" x2="1" y2="1">
        <stop offset="0" stop-color="var(--teal-deep)"/>
        <stop offset="0.5" stop-color="var(--teal)"/>
        <stop offset="1" stop-color="var(--teal-light)"/>
      </linearGradient>
      <radialGradient id="medal-face" cx="0.4" cy="0.35" r="0.75">
        <stop offset="0" stop-color="var(--gold-light)"/>
        <stop offset="0.6" stop-color="var(--gold)"/>
        <stop offset="1" stop-color="var(--gold-deep)"/>
      </radialGradient>
    </defs>
    <polygon points="575,0 610,0 790,1200 760,1200" fill="var(--teal-light)" opacity="0.35"/>
    <polygon points="615,0 700,0 851,1010 851,1200 800,1200" fill="url(#gold-band)"/>
    <polygon points="700,0 851,0 851,1010" fill="url(#teal-band)"/>
    <polygon points="698,0 708,0 851,960 851,990" fill="#ffffff" opacity="0.8"/>
    <polygon points="790,400 851,520 851,1200 830,1200" fill="url(#teal-band)" opacity="0.9"/>

    <g class="medal">
      <circle cx="723" cy="405" r="100" fill="var(--gold-deep)"/>
      <circle cx="723" cy="405" r="92" fill="url(#medal-face)"/>
      <circle cx="723" cy="405" r="80" fill="none" stroke="#ffffff" stroke-width="2" opacity="0.7"/>
      <g fill="#ffffff">
        <polygon points="698,352 701,360 709,360 703,365 705,373 698,368 691,373 693,365 687,360 695,360"/>
        <polygon points="723,344 726,352 734,352 728,357 730,365 723,360 716,365 718,357 712,352 720,352"/>
        <polygon points="748,352 751,360 759,360 753,365 755,373 748,368 741,373 743,365 737,360 745,360"/>
        <polygon points="713,450 715,455 720,455 716,458 717,463 713,460 709,463 710,458 706,455 711,455"/>
        <polygon points="733,450 735,455 740,455 736,458 737,463 733,460 729,463 730,458 726,455 731,455"/>
      </g>
      <text x="723" y="427" text-anchor="middle" font-family="Noto Sans JP, sans-serif" font-size="58" font-weight="900" fill="#ffffff" letter-spacing="2">初級</text>
    </g>
  </svg>

  <h1 class="certificate__title">認定証</h1>
  <p class="certificate__qualification">発達障がい支援アドバイザー</p>

  <div class="certificate__recipient">
    <span class="certificate__name">●●</span>
    <span class="certificate__honorific">殿</span>
  </div>

  <p class="certificate__date">●●年●月●日</p>

  <p class="certificate__statement">あなたは当カリキュラムを修了されましたので、<br>『初級・発達障がい支援アドバイザー』として<br>認定いたします。</p>

  <div class="issuer">
    <span class="issuer__mark"></span>
    <span class="issuer__name">NPO法人青葉学習推進会</span>
  </div>
</main>
</body>
</html>
```